'TOLVANTA' NEW WINE LABEL DESIGN

I am looking for an exceptional and exciting design for a wine label called 'Tolvanta' meaning 'Lookout'. The design must feature the name 'Tolvanta', and the word 'Cabernet Sauvignon' in version 1 and 'Sauvignon Blanc' in version 2. It will also need the words 'Valle Central, Chile' at the bottom of the label as a prominent piece of information as well as the vintage 2017. Please produce the work in size 80mm x 100mm. Feel free to use colour in addition to black/white and ensue that the label is easy to read on a shelf placement.
Target Market(s)
SUPERMARKETS & WINE STORES
Requirements
Must have
- EASY TO READ, USE COLOURS LIKE GREEN FOR SAUVIGNON & RED FOR CABERNET SAUVIGNON
- FULL BOTTLE SHOT MUST BE IN PROVIDED DESIGNS. ALL BOTTLE TOPS SHOULD BE QUORLAN STYLE (SCREW TOP)
- PLEASE NOTE THAT LABEL INFORMATION MUSY BE EASY TO READ I.E. VINTAGE, PLACE OF ORGIN ALTHOUGH NOT THE MAIN CONTENT MUST STILL BE CLEAR.
Nice to have
- ARTISTIC REFERENCE LINK TO NAME & ANDES BUT NOT PICTURES OF MOUNTAINS
Should not have
- PICTURES OF GRAPES
- PICTURES OF VINEYARDS
- PICTURES OF MOUNTAINS

```html
<!DOCTYPE html>
<html lang="en">
<head>
<meta charset="utf-8">
<title>Tolvanta Wine Labels</title>
<link rel="stylesheet" href="https://fonts.googleapis.com/css2?family=Fira+Sans:wght@300;400&display=swap">
<style>
  :root {
    --stage: #2a1d17;
    --cab-ground: #050404;
    --cab-ink: #f2eeea;
    --cab-accent: #c4161c;
    --cab-accent-deep: #5a0b0e;
    --blanc-ground: #94d7c5;
    --blanc-ink: #34473a;
    --blanc-accent: #f4fbf8;
  }
  * { margin: 0; padding: 0; box-sizing: border-box; }
  html, body {
    width: 1189px;
    height: 1200px;
    overflow: hidden;
    background: var(--stage);
  }
  .label-set {
    position: relative;
    width: 1189px;
    height: 1200px;
  }
  .label {
    position: absolute;
    top: 258px;
    width: 440px;
    height: 684px;
    overflow: hidden;
    font-family: "Fira Sans", sans-serif;
    font-weight: 300;
  }
  .label--cabernet { left: 104px; background: var(--cab-ground); color: var(--cab-ink); }
  .label--blanc { left: 644px; background: var(--blanc-ground); color: var(--blanc-ink); }

  .label__pattern {
    position: absolute;
    right: 0;
    top: 44px;
    width: 250px;
    height: 640px;
    border-radius: 120px 0 0 0;
  }
  .label--cabernet .label__pattern {
    background: radial-gradient(ellipse at 60% 55%, var(--cab-accent) 0%, var(--cab-accent-deep) 55%, rgba(5,4,4,0) 85%);
    opacity: 0.85;
  }
  .label--blanc .label__pattern {
    background: radial-gradient(ellipse at 60% 55%, var(--blanc-accent) 0%, rgba(244,251,248,0.55) 50%, rgba(148,215,197,0) 85%);
  }

  .label__brand {
    position: absolute;
    left: 24px;
    top: 52px;
    font-size: 34px;
    font-weight: 400;
    letter-spacing: 5px;
    line-height: 1;
  }
  .label--cabernet .label__brand { color: var(--cab-accent); }
  .label--blanc .label__brand { color: var(--blanc-ink); }

  .label__varietal {
    position: absolute;
    left: 20px;
    top: 252px;
    font-size: 58px;
    line-height: 64px;
    letter-spacing: 1.5px;
  }
  .label__origin {
    position: absolute;
    left: 24px;
    top: 420px;
    font-size: 18px;
    line-height: 20px;
    font-weight: 400;
  }
  .label__vintage {
    position: absolute;
    left: 22px;
    bottom: 34px;
    font-size: 28px;
    font-weight: 400;
  }
</style>
</head>
<body>
  <main class="label-set">
    <section class="label label--cabernet">
      <div class="label__pattern" role="img" aria-label="Red flowing swirl ornament rising like wind over peaks"></div>
      <div class="label__brand">TOLVANTA</div>
      <h1 class="label__varietal">Cabernet<br>Sauvignon</h1>
      <p class="label__origin">Valle Central<br>Chile</p>
      <p class="label__vintage">2017.</p>
    </section>

    <section class="label label--blanc">
      <div class="label__pattern" role="img" aria-label="White flowing swirl ornament rising like wind over peaks"></div>
      <div class="label__brand">TOLVANTA</div>
      <h1 class="label__varietal">Sauvignon<br>Blanc</h1>
      <p class="label__origin">Valle Central<br>Chile</p>
      <p class="label__vintage">2017.</p>
    </section>
  </main>
</body>
</html>
```